Etiketten für Gin
Zielgruppe
Wir vertreiben einen regionalen Gin mit Fichtennadeln.
Zielgruppe sind Gin-Trinker, Wanderer, Besucher und Bewohner der Bergischen Landes.
Aufgabenstellung
Benötigt wird ein zweiteiliges Etikett für eine 500 ml Flasche (Höhe 320 mm, Durchmesser ca. 75 mm). Datenblatt in der Anlage. Die Flasche wird einen schwarzen Stopfen bekommen,
Das vordere Etikett soll eine Größe von 80 mm (Breite) x 160 mm (Höhe) haben. Das Etikett für die Rückseite soll eine Größe von 60 mm (Breite) x 100 mm (Höhe) haben.
Aufgrund des schwarzen Stopfens wird ein Etikett mit/in schwarz favorisiert. Auf der Vorderseite soll unser Logo (bei den Dateien) abgebildet sein.
Pflichtangaben Vorderseite: auf dem vorderen Etikett müssen die Pflichtangaben zur Nettofüllmenge und zum Alkoholgehalt angegeben sein. Sprich, auf der Vorderseite muss 500 ml und 43 % untergebracht sein. Diese Pflichtangaben müssen zwingend eine Höhe von 4 mm haben (gesetzlich vorgeschrieben). Gleiches gilt für die Verkehrsbezeichnung Gin, die im Logo enthalten ist. Das Wort Gin muss ebenfalls eine Größe von mindestens 4 mm haben.
Auf dem rückwärtigen Etikett müssen folgende Pflichtangaben vorhanden sein:
Talwerk Brand
Lukas Dornfeld
Anton-Weller-Straße 27
51467 Bergisch Gladbach
Des Weiteren wären auf der Rückseite zwei Felder wünschenswert, in die man zum einen die Batch No. und zum anderen die Flaschennummer eintragen kann (Beispiel Bild 'Batch_Flasche'). Zudem ein weißes Feld, in dem später der EAN Code Ei gepflegt werden kann.
Als Text für die Rückseite:
Wo Natur auf Geschmack trifft
Das 'Bergische Gefühl' erleben Sie mit dem Talwerk Brand Gin. Lassen Sie einen naturverbundenen Tag zum Ausklang, beispielsweise nach einer Wanderung, noch einmal an Ihnen vorbeiziehen.
Erinnern Sie sich durch die bei der Herstellung geschmacksgebenden Botanicals von der Fichte an einen erholsamen Spaziergang durch die Wälder des Bergischen Landes.
Mehr Informationen unter
www.talwerk-brand.de
Druckdatenanlieferung laut Druckerei:
Dateiform..

```html
<!DOCTYPE html>
<html lang="de">
<head>
<meta charset="utf-8">
<title>Talwerk Brand Gin – Etikettenvarianten</title>
<link rel="stylesheet" href="https://fonts.googleapis.com/css2?family=Poiret+One&family=Oswald:wght@400&family=Montserrat:wght@400&display=swap">
<style>
  :root {
    --bg: #ffffff;
    --cream: #f4f2ea;
    --mint: #cfe6b8;
    --leaf: #5fae45;
    --forest: #2f8a3a;
    --deep: #0f6b3a;
    --pine: #1d4f33;
    --night: #22302a;
    --ink: #1f2a24;
    --white: #ffffff;
    --caption: #b9b9b9;
  }
  * { box-sizing: border-box; margin: 0; padding: 0; }
  html, body { width: 1200px; height: 800px; overflow: hidden; background: var(--bg); }
  .lineup {
    position: absolute; left: 40px; top: 250px;
    display: flex; gap: 30px;
  }
  .variant { width: 200px; display: flex; flex-direction: column; align-items: center; }
  .label {
    position: relative; width: 200px; height: 228px; overflow: hidden;
    color: var(--white);
    box-shadow: 0 1px 3px rgba(0,0,0,.15);
  }
  .forest { position: absolute; left: 0; right: 0; }
  .seal {
    position: absolute; left: 50%; top: 26px; width: 64px; height: 64px;
    margin-left: -32px; border-radius: 50%;
    border: 2px solid var(--white); background: rgba(255,255,255,.15);
  }
  .brand {
    position: absolute; left: 0; right: 0; top: 118px; text-align: center;
    font-family: "Poiret One", sans-serif; font-size: 22px; letter-spacing: .5px;
    color: var(--white);
  }
  .denomination {
    position: absolute; left: 0; right: 0; top: 146px; text-align: center;
    font-family: "Montserrat", sans-serif; font-size: 9px; letter-spacing: 3px;
  }
  .facts {
    position: absolute; left: 14px; right: 14px; bottom: 14px;
    display: flex; justify-content: space-between;
    font-family: "Oswald", sans-serif; font-size: 9px; color: var(--white);
  }
  .caption {
    margin-top: 110px;
    font-family: "Montserrat", sans-serif; font-size: 20px; color: var(--caption);
  }

  /* Variante 010 */
  .v010 { background: var(--cream); }
  .v010 .forest { top: 60px; bottom: 0;
    background: linear-gradient(180deg, rgba(95,174,69,0) 0%, var(--leaf) 35%, var(--forest) 70%, var(--deep) 100%); }
  .v010 .seal { border-color: var(--pine); background: var(--mint); }

  /* Variante 020 */
  .v020 { background: var(--mint); }
  .v020 .forest { top: 0; bottom: 0;
    background: linear-gradient(180deg, #e4f1d6 0%, #8cc66d 30%, var(--forest) 65%, var(--deep) 100%); }

  /* Variante 030 */
  .v030 { background: var(--deep); }
  .v030 .forest { top: 0; height: 205px;
    background: linear-gradient(180deg, #dcedc8 0%, #86c36a 30%, var(--forest) 65%, #16714a 100%); }
  .v030 .base-band { position: absolute; left: 0; right: 0; bottom: 0; height: 23px; background: var(--pine); }
  .v030 .brand { top: 124px; }
  .v030 .denomination { top: 152px; }
  .v030 .facts { top: 156px; bottom: auto; }

  /* Variante 040 */
  .v040 { background: var(--night); }
  .v040 .forest { top: 0; height: 40px;
    background: linear-gradient(180deg, #bfe0a4 0%, var(--leaf) 60%, var(--forest) 100%); }
  .v040 .seal { top: 50px; border-color: var(--leaf); background: var(--pine); }
  .v040 .base-band { position: absolute; left: 0; right: 0; bottom: 0; height: 38px;
    background: linear-gradient(180deg, #1d6b44, var(--deep)); }
  .v040 .brand { top: 134px; }
  .v040 .denomination { top: 162px; color: var(--leaf); }
  .v040 .facts { top: 166px; bottom: auto; }

  /* Variante 050 */
  .v050 { background: var(--white); border: 1px solid #e6e6e6; }
  .v050 .forest { top: 50px; bottom: 0; left: 0; right: 0;
    background: linear-gradient(90deg, var(--forest) 0%, #7fbf68 35%, rgba(207,230,184,.6) 70%, rgba(255,255,255,0) 100%); }
  .v050 .seal { border-color: var(--pine); background: var(--mint); }
  .v050 .brand { color: var(--ink); top: 122px; }
  .v050 .denomination { top: 150px; color: var(--leaf); }
</style>
</head>
<body>
<main class="lineup">
  <section class="variant">
    <div class="label v010">
      <div class="forest" role="img" aria-label="Fichtenwald-Illustration in Grüntönen"></div>
      <div class="seal"></div>
      <p class="brand">TALWERK BRAND</p>
      <p class="denomination">· GIN ·</p>
      <div class="facts"><span>500ML</span><span>43% VOL</span></div>
    </div>
    <p class="caption">NUMBER -010</p>
  </section>

  <section class="variant">
    <div class="label v020">
      <div class="forest" role="img" aria-label="Nebliger Fichtenwald in Grünverlauf"></div>
      <div class="seal"></div>
      <p class="brand">TALWERK BRAND</p>
      <p class="denomination">· GIN ·</p>
      <div class="facts"><span>500ML</span><span>43% VOL</span></div>
    </div>
    <p class="caption">NUMBER -020</p>
  </section>

  <section class="variant">
    <div class="label v030">
      <div class="forest" role="img" aria-label="Nebliger Fichtenwald in Grünverlauf"></div>
      <div class="base-band"></div>
      <div class="seal"></div>
      <p class="brand">TALWERK BRAND</p>
      <p class="denomination">· GIN ·</p>
      <div class="facts"><span>500ML</span><span>43% VOL</span></div>
    </div>
    <p class="caption">NUMBER -030</p>
  </section>

  <section class="variant">
    <div class="label v040">
      <div class="forest" role="img" aria-label="Schmaler Streifen Fichtenwald-Silhouette"></div>
      <div class="base-band"></div>
      <div class="seal"></div>
      <p class="brand">TALWERK BRAND</p>
      <p class="denomination">· GIN ·</p>
      <div class="facts"><span>500ML</span><span>43% VOL</span></div>
    </div>
    <p class="caption">NUMBER -040</p>
  </section>

  <section class="variant">
    <div class="label v050">
      <div class="forest" role="img" aria-label="Fichtenbäume am linken Rand, nach rechts auslaufend"></div>
      <div class="seal"></div>
      <p class="brand">TALWERK BRAND</p>
      <p class="denomination">· GIN ·</p>
      <div class="facts"><span>500ML</span><span>43% VOL</span></div>
    </div>
    <p class="caption">NUMBER -050</p>
  </section>
</main>
</body>
</html>
```